Miami based company needs a HTML creative 1 page web design

Our company, Calvanta Systems need a 1 page web design for a service that we offer, namely keyvaultportal.net. It is essentially a client portal. We provide a new an exciting service for Title Companies. Instead of the closing agent handing out a paper copy of the closing documents, the buyer of the home is able to log into keyvaultportal.net and view their closing documents 24/7 on a secure site. When the buyer logs in, they are also able to view the contact information for the real estate agent, lender, and that actual closing agent that was involved in the transaction.
Here is the link to our current site:
www.keyvaultportal.net
USERNAME = 0473612
PASSWORD = morley@calvanta.net
We want the site to be more creative and have a nice fresh, clean and new look. We are catering to the real estate industry so images, vectors etc could be real estate or housing related. We don't want it to look just like our current site. We need all the elements but want a creative new design with different colors (not necessarily green). The current site should just be used as a general guide.
It is also important to note that the colors should be relatively neutral as the site will be branded for each one of our clients (the title company). Unlike our current site, the title company's logo should be up top, not the Key Vault Portal logo. We want it to look like it is coming from the title company. Our logo, should be on the bottom and say "powered by KeyVaultPortal.net".
It is important to note that we will be loading information dynamically for the following. We wrote the code for loading it in, we just need the place holders:
1.) The title company - logo, website, phone, fax, address. The site should be branded to the Title Company.
2.) Key Vault Portal - will have PDF files that the title company uploads.
3.) The Lender - possible picture, company name, email and phone
4.) The Real Estate Agent - possible picture, company name, email and phone
5.) The Title Agent - possible picture, email and phone
Other things to note:
1.) A user may have multiple transactions. Therefore the information for the closing package, real estate agent, lender and title agent will need to be able to stack. For example, on our current site, the green accordion will stack if there are multiple transactions.
2.) It is also important to note that sometimes there wont be any information for the broker or real estate agent or title agent. On our current site for example, if there is no real estate agent, that tab is not visible.
3.) This page will be viewed on mobile, tablets and computers and will need to be designed so it can be viewed on these.
If you have any questions, please don't hesitate to contact me.
Thanks and looking forward to seeing your work.
-Dale
Target Market(s)
Our client is the title company. The consumers that will be logging in our the customers of the title company (the consumers that purchased real estate and closed at the title company).
Industry/Entity Type
Real Estate
Number of Pages Required
1 page
Look and feel

```html
<!DOCTYPE html>
<html lang="en">
<head>
<meta charset="utf-8">
<title>KeyVaultPortal.net</title>
<link href="https://fonts.googleapis.com/css2?family=Questrial&family=Open+Sans:ital,wght@0,400;0,600;1,400;1,600&display=swap" rel="stylesheet">
<style>
:root{
  --green:#5aab3b;
  --green-dark:#3f8a26;
  --ink:#333333;
  --muted:#6b6b6b;
  --dark:#2b2b2b;
  --darker:#232323;
  --footer:#353535;
  --line:#d9d9d9;
  --white:#ffffff;
}
*{box-sizing:border-box;margin:0;padding:0}
html,body{width:818px;height:1200px;overflow:hidden;background:var(--white)}
body{position:relative;font-family:"Open Sans",sans-serif;color:var(--ink)}
.abs{position:absolute}
.display{font-family:"Questrial",sans-serif}

/* header */
.site-header{left:0;top:0;width:818px;height:80px;background:var(--white);box-shadow:0 2px 6px rgba(0,0,0,.06);z-index:2}
.brand{left:77px;top:14px;display:flex;align-items:center;gap:10px}
.brand-mark{width:50px;height:50px;border-radius:50%;border:5px solid var(--green)}
.brand-name{font-family:"Questrial",sans-serif;font-size:18px;color:var(--ink)}
.social-top{left:612px;top:20px;display:flex;gap:7px}
.social-top span{width:21px;height:21px;border-radius:50%;background:#c9c9c9}
.tagline{left:537px;top:49px;font-size:10px;color:#8a8a8a}

/* hero */
.hero{left:0;top:80px;width:818px;height:322px;background:linear-gradient(90deg,#f4f4f2 0%,#ecebe8 50%,#e6e4e0 100%)}
.hero h1{left:88px;top:72px;font-weight:400;font-size:21px;line-height:31px;color:var(--ink)}
.hero h1 em{font-style:normal;color:var(--green)}
.hero p{left:88px;top:136px;width:310px;font-size:10px;line-height:15px;color:#555}
.btn-download{left:88px;top:213px;width:140px;height:34px;background:var(--green);color:var(--white);font-size:12px;display:flex;align-items:center;gap:10px;padding-left:8px}
.btn-download svg{flex:none}
.tablet{left:488px;top:42px;width:242px;height:280px;border-radius:14px 14px 0 0;background:linear-gradient(180deg,#2a2a2a,#1a1a1a)}
.tablet-screen{left:13px;top:40px;width:216px;height:240px;background:linear-gradient(180deg,#f7f7f7,#e9e9e9)}

/* section marker */
.section-marker{left:396px;width:26px;height:26px;border-radius:50%;border:2px solid #9a9a9a}

/* packages */
.packages{left:0;top:402px;width:818px;height:398px;background:linear-gradient(180deg,#2f2f2f,#262626)}
.packages h2{left:0;top:62px;width:818px;text-align:center;font-weight:400;font-size:21px;color:var(--white)}
.packages .lede{left:160px;top:95px;width:498px;text-align:center;font-style:italic;font-size:10px;line-height:15px;color:#a8a8a8}
.tabs{left:74px;top:150px;width:164px}
.tab{height:36px;background:#f1f1f1;border-bottom:1px solid var(--line);font-family:"Questrial",sans-serif;font-size:13px;color:var(--ink);padding:10px 10px}
.tab.active{position:relative;background:var(--green);color:var(--white);margin-left:-12px;width:188px;height:38px}
.tab.active:after{content:"";position:absolute;right:-12px;top:0;border-left:12px solid var(--green);border-top:19px solid transparent;border-bottom:19px solid transparent}
.tab.active:before{content:"";position:absolute;left:0;bottom:-6px;border-top:6px solid var(--green-dark);border-left:12px solid transparent}
.contact{left:266px;top:150px;width:300px;color:#b5b5b5}
.contact h3{font-family:"Questrial",sans-serif;font-weight:400;font-size:14px;color:var(--white);margin-bottom:4px}
.contact .bio{font-style:italic;font-size:9.5px;line-height:13.5px;color:#8e8e8e;margin-bottom:9px}
.contact dl{font-size:10px;line-height:19px}
.contact dt{display:inline;margin-right:10px}
.contact dd{display:inline;color:var(--green)}
.portrait{left:585px;top:150px;width:157px;height:214px;background:linear-gradient(180deg,#6f7a4b,#3b3f31)}

/* testimonials */
.testimonials{left:0;top:800px;width:818px;height:233px;background:linear-gradient(180deg,#ffffff,#f1f1f1)}
.testimonials h2{left:0;top:64px;width:818px;text-align:center;font-weight:400;font-size:20px;color:var(--ink)}
.quote{top:112px;width:300px}
.quote .mark{position:absolute;font-family:Georgia,serif;font-size:60px;color:#e2e2e2;line-height:1}
.quote .open{left:0;top:-12px}
.quote .close{left:178px;top:40px}
.quote p{position:relative;font-style:italic;font-size:10px;line-height:15px;color:#8a8a8a;padding-left:12px}
.quote cite{position:relative;display:block;margin-top:12px;padding-left:12px;font-weight:600;font-style:italic;font-size:10px;color:var(--green)}

/* newsletter */
.newsletter{left:0;top:1033px;width:818px;height:127px;background:var(--footer)}
.newsletter .lead{left:75px;top:41px;font-family:"Questrial",sans-serif;font-size:11px;color:#d8d8d8}
.newsletter .field{left:75px;top:58px;width:295px;height:22px;background:var(--white);border:1px solid #ccc;font-family:Georgia,serif;font-size:11px;color:#777;padding:3px 5px}
.newsletter .subscribe{left:379px;top:58px;width:74px;height:22px;background:var(--green);color:var(--white);font-size:10px;font-weight:600;display:flex;align-items:center;justify-content:center}
.footer-icons{left:540px;top:50px;display:flex;gap:20px;align-items:center}
.legal{left:0;top:1160px;width:818px;height:40px;background:var(--darker);font-size:8.5px;color:#9a9a9a}
.legal .copy{left:75px;top:15px}
.legal .links{right:75px;top:15px}
</style>
</head>
<body>

<header class="site-header abs">
  <div class="brand abs"><span class="brand-mark"></span><span class="brand-name">KeyVaultPortal.net</span></div>
  <div class="social-top abs"><span></span><span></span><span></span><span></span><span></span></div>
  <div class="tagline abs display">Your Closing Documents And Your Fingertips</div>
</header>

<section class="hero abs" role="img" aria-label="Soft blurred background photo of a home interior">
  <h1 class="abs display">Welcome To <em>Key Vault Portal</em><br>The Key To Real Estate Marketing</h1>
  <p class="abs">Lorem ipsum dolor sit amet, consectetur adipiscing elit, sed do eiusmod tempor incididunt ut labore et dolore magna aliqua. Ut enim ad minim veniam, quis nostrud exercitation ullamco laboris nisi ut aliquip ex ea commodo consequat..</p>
  <a class="btn-download abs display">
    <svg width="24" height="26" viewBox="0 0 24 26"><path d="M2 1h14l6 6v18H2z" fill="#fff"/><path d="M16 1v6h6" fill="#ddd"/><rect x="0" y="4" width="13" height="6" fill="#d33"/></svg>
    Download Now
  </a>
  <div class="tablet abs" role="img" aria-label="Tablet showing a purchase contract document">
    <div class="tablet-screen abs"></div>
  </div>
</section>

<section class="packages abs" role="img" aria-label="Dark tinted background photo of a document signing">
  <span class="section-marker abs" style="top:24px"></span>
  <h2 class="abs display">Your Key Vault Portal(S)</h2>
  <p class="lede abs">Lorem ipsum dolor sit amet, consectetur adipiscing elit, sed do eiusmod tempor incididunt ut labore et dolore magna aliqua ut enim ad minim ut aliquip ex ea commodo consequat..</p>
  <nav class="tabs abs">
    <div class="tab">Closing Package</div>
    <div class="tab active">Real Estate Agent</div>
    <div class="tab">Loan Officer</div>
    <div class="tab">Title Agent</div>
  </nav>
  <div class="contact abs">
    <h3>Real Estate Agent</h3>
    <p class="bio">Lorem ipsum dolor sit amet, consectetur adipiscing elit, sed do eiusmod tempor incididunt ut labore et dolore magna aliqua. Ut enim ad minim veniam, quis nostrud exercitation ullamco laboris nisi ut aliquip ex ea commodo consequat.</p>
    <dl>
      <div>Martin Ashdale</div>
      <div>Ashdale Realty</div>
      <div><dt>Email:</dt><dd>m@ashdalerealty.com</dd></div>
      <div><dt>Website:</dt><dd>www.ashdalerealty.com</dd></div>
      <div><dt>Phone:</dt><dd>305-555-0187</dd></div>
    </dl>
  </div>
  <div class="portrait abs" role="img" aria-label="Portrait photo of the real estate agent"></div>
</section>

<section class="testimonials abs">
  <span class="section-marker abs" style="top:28px"></span>
  <h2 class="abs display">What Our Client Say's</h2>
  <blockquote class="quote abs" style="left:77px">
    <span class="mark open">&ldquo;</span>
    <span class="mark close">&rdquo;</span>
    <p>Lorem ipsum dolor sit amet, consectetur adipiscing elit, sed do eiusmod tempor incididunt ut labore et dolore magna aliqua. Ut enim ad minim veniam, quis nostrud exercitation ullamco laboris nisi ut aliquip ex ea commodo consequat.</p>
    <cite>Renata Holm</cite>
  </blockquote>
  <blockquote class="quote abs" style="left:433px">
    <span class="mark open">&ldquo;</span>
    <span class="mark close">&rdquo;</span>
    <p>Lorem ipsum dolor sit amet, consectetur adipiscing elit, sed do eiusmod tempor incididunt ut labore et dolore magna aliqua. Ut enim ad minim veniam, quis nostrud exercitation ullamco laboris nisi ut aliquip ex ea commodo consequat.</p>
    <cite>Renata Holm</cite>
  </blockquote>
</section>

<section class="newsletter abs">
  <div class="lead abs">Join 8,000 Smart Owners Who Get Our Emails Every Month. Be Better In 2014.</div>
  <div class="field abs">name@example.com</div>
  <div class="subscribe abs">SUBCRIBE</div>
  <div class="footer-icons abs">
    <svg width="16" height="26" viewBox="0 0 16 26"><rect x="1" y="1" width="14" height="24" rx="2" fill="none" stroke="#fff" stroke-width="2"/><rect x="4" y="5" width="8" height="13" fill="#fff"/></svg>
    <span style="width:24px;height:24px;border-radius:50%;background:#fff"></span>
    <span style="width:24px;height:24px;background:#fff"></span>
    <span style="width:24px;height:24px;border-radius:50%;background:#fff"></span>
    <svg width="26" height="24" viewBox="0 0 26 24"><rect x="1" y="1" width="24" height="22" fill="none" stroke="#fff" stroke-width="2"/><path d="M1 1 L25 23 M25 1 L1 23" stroke="#fff" stroke-width="2"/></svg>
  </div>
</section>

<footer class="legal abs">
  <div class="copy abs">Copyrights &copy; 2015 KeyVaultPortal.net - All Rights Reserved</div>
  <div class="links abs">Privacy Policy &nbsp; | &nbsp; Term &amp; Conditions</div>
</footer>

</body>
</html>
```